New Record Label needs a Web design

We are Iron Heron: a London based, new & independent music production company aimed at the 25-40 age group. The musical style is Soul/Classic Brelvane.
We have at the moment just one signed artist, but will expand in the future.
We dont' have any webpage yet and are looking for an innovative web design for our webpage www.iron-heron-example.com
I have uploaded our company logo.

Initially the whole website will only have 3 tabs: Home page/Artists/Contact

The design should be classic and high-end, but can be a bit crazy too.

```html
<!DOCTYPE html>
<html lang="en">
<head>
<meta charset="utf-8">
<title>Iron Heron – Artists</title>
<link rel="stylesheet" href="https://fonts.googleapis.com/css2?family=Antonio:wght@200;400&display=swap">
<style>
  :root {
    --backdrop: #e8b5a0;
    --paper: #ffffff;
    --brick: #c63a3a;
    --ember: #d4693f;
    --outline-white: #ffffff;
  }
  html, body {
    margin: 0;
    width: 1200px;
    height: 1000px;
    overflow: hidden;
    background: var(--backdrop);
  }
  .page {
    position: relative;
    width: 1200px;
    height: 1000px;
  }
  .card {
    position: absolute;
    left: 35px;
    top: 75px;
    width: 1132px;
    height: 850px;
    background: var(--paper);
    box-shadow: 0 2px 8px rgba(0,0,0,0.25);
  }
  .artboard {
    position: absolute;
    left: 0;
    top: 0;
  }
  .brand {
    position: absolute;
    left: 60px;
    top: 190px;
    width: 350px;
    display: flex;
    align-items: center;
    justify-content: center;
    gap: 14px;
    font-family: "Antonio", sans-serif;
    font-weight: 400;
    font-size: 52px;
    line-height: 1;
    color: var(--brick);
    letter-spacing: 2px;
  }
  .brand-dot {
    width: 26px;
    height: 26px;
    border-radius: 50%;
    background: var(--ember);
  }
  .outline-title {
    font-family: "Antonio", sans-serif;
    font-weight: 400;
    text-transform: uppercase;
    fill: none;
  }
  .section-title {
    font-size: 104px;
    stroke: var(--brick);
    stroke-width: 2;
  }
  .artist-name {
    font-size: 48px;
    stroke: var(--outline-white);
    stroke-width: 1.6;
  }
  .social {
    position: absolute;
    display: flex;
    gap: 10px;
  }
  .social-dot {
    width: 48px;
    height: 48px;
    border-radius: 50%;
    background: var(--paper);
  }
  .social-one { left: 976px; top: 284px; }
  .social-two { left: 533px; top: 523px; }
  .social-two .social-dot { background: var(--brick); }
  .social-two .social-dot:nth-child(2) { background: var(--ember); }
  .social-three { left: 783px; top: 749px; }
</style>
</head>
<body>
<main class="page">
  <section class="card" aria-label="Artists page"></section>

  <svg class="artboard" width="1200" height="1000" viewBox="0 0 1200 1000">
    <defs>
      <linearGradient id="records" x1="0" y1="0" x2="1" y2="1">
        <stop offset="0" stop-color="#8a6a5a"/>
        <stop offset="0.5" stop-color="#c9b8a8"/>
        <stop offset="1" stop-color="#3c3a44"/>
      </linearGradient>
      <linearGradient id="stage-one" x1="0" y1="0" x2="1" y2="0">
        <stop offset="0" stop-color="#d63fe8"/>
        <stop offset="1" stop-color="#f0407a"/>
      </linearGradient>
      <linearGradient id="stage-two" x1="0" y1="0" x2="1" y2="0">
        <stop offset="0" stop-color="#16123e"/>
        <stop offset="0.55" stop-color="#5a2db8"/>
        <stop offset="1" stop-color="#3a2a9a"/>
      </linearGradient>
      <linearGradient id="stage-three" x1="0" y1="0" x2="1" y2="0">
        <stop offset="0" stop-color="#6a1fb0"/>
        <stop offset="0.55" stop-color="#b93fc8"/>
        <stop offset="1" stop-color="#e8883a"/>
      </linearGradient>
    </defs>

    <g role="img" aria-label="Close-up of vinyl records in a crate">
      <polygon points="1090,580 1167,580 1167,925 230,925 262,838 1062,838" fill="url(#records)"/>
    </g>

    <polygon class="left-block" points="35,500 390,500 240,862 35,862" fill="var(--brick)"/>
    <polygon class="top-band" points="585,75 1167,75 1167,110 572,110" fill="var(--brick)"/>

    <g role="img" aria-label="Singer performing with a microphone under pink stage light">
      <polygon points="590,110 1040,110 940,345 475,345" fill="url(#stage-one)"/>
    </g>
    <polygon class="panel" points="1040,110 1167,110 1167,345 940,345" fill="var(--ember)"/>

    <g role="img" aria-label="Singer leaning into the microphone under blue and violet light">
      <polygon points="800,345 1167,345 1167,580 705,580" fill="url(#stage-two)"/>
    </g>

    <g role="img" aria-label="Singer in a cap and glasses singing into a microphone">
      <polygon points="385,580 840,580 740,815 285,815" fill="url(#stage-three)"/>
    </g>
    <polygon class="panel" points="840,580 1167,580 1090,815 740,815" fill="var(--ember)"/>

    <polygon class="bottom-band" points="270,815 1072,815 1062,838 262,838" fill="var(--brick)"/>

    <text class="outline-title section-title" x="40" y="494" textLength="350" lengthAdjust="spacing">Artists</text>

    <text class="outline-title artist-name" x="793" y="176" textLength="117" lengthAdjust="spacing">Lorem</text>
    <text class="outline-title artist-name" x="870" y="222" textLength="106" lengthAdjust="spacing">Ipsum</text>

    <text class="outline-title artist-name" x="736" y="570" textLength="246" lengthAdjust="spacing">Lorem Ipsum</text>

    <text class="outline-title artist-name" x="620" y="650" textLength="118" lengthAdjust="spacing">Lorem</text>
    <text class="outline-title artist-name" x="658" y="697" textLength="108" lengthAdjust="spacing">Ipsum</text>
  </svg>

  <div class="brand"><span class="brand-dot"></span>IRON HERON</div>

  <div class="social social-one"><span class="social-dot"></span><span class="social-dot"></span><span class="social-dot"></span></div>
  <div class="social social-two"><span class="social-dot"></span><span class="social-dot"></span><span class="social-dot"></span></div>
  <div class="social social-three"><span class="social-dot"></span><span class="social-dot"></span><span class="social-dot"></span></div>
</main>
</body>
</html>
```